Tailbrook Website Design

Need a website for a Dog Grooiming business. Please make it simular to these:

https://www.furvanto.com
https://haulnorix.com
https://meadowpetrin.com
https://www.drivelumo.com/search/

```html
<!DOCTYPE html>
<html lang="en">
<head>
<meta charset="utf-8">
<title>Tailbrook — Dog Grooming</title>
<link href="https://fonts.googleapis.com/css2?family=Outfit:wght@300;400;500;600;700&display=swap" rel="stylesheet">
<style>
:root{
  --green-dark:#0d5a4a;
  --green-mid:#146552;
  --mint:#d6e5dc;
  --mint-deep:#cddfd4;
  --mint-card:#dfeae3;
  --grey-bg:#eef1f2;
  --orange:#fa8a6a;
  --ink:#1f3b35;
  --text:#4a5c57;
  --white:#ffffff;
}
*{box-sizing:border-box;margin:0;padding:0}
html,body{width:1200px;height:4127px;overflow:hidden}
body{position:relative;font-family:"Outfit",sans-serif;color:var(--text);background:var(--white)}
.abs{position:absolute}
.btn{position:absolute;display:flex;align-items:center;justify-content:center;background:var(--orange);color:var(--white);border-radius:20px;font-size:12px;font-weight:600;text-decoration:none}
.h2{font-weight:600;color:var(--green-dark);font-size:35px;line-height:41px}
.photo{position:absolute}
.brand{display:flex;align-items:center;gap:10px;font-weight:600;color:var(--green-dark);font-size:24px}
.brand-dot{width:22px;height:22px;border-radius:50%;background:var(--orange)}
.phone{position:absolute;display:flex;gap:8px;align-items:flex-start;color:var(--green-dark)}
.phone strong{display:block;font-size:17px;font-weight:600;line-height:18px}
.phone small{display:block;font-size:11px;color:var(--text)}

.nav{position:absolute;left:334px;top:34px;display:flex;gap:30px;font-size:12px;color:var(--green-dark)}
.hero{position:absolute;left:0;top:0;width:1200px;height:666px;background:var(--mint)}
.hero-band{position:absolute;left:0;top:556px;width:1200px;height:110px;background:var(--mint-deep)}
.hero-kicker{left:159px;top:212px;font-size:24px;color:var(--green-dark)}
.hero-title{left:159px;top:240px;font-size:58px;line-height:58px;font-weight:700;color:var(--green-dark)}
.hero-text{left:160px;top:378px;width:265px;font-size:13px;line-height:20px}
.quote{position:absolute;left:497px;top:213px;width:336px;height:386px;background:var(--green-dark);border-radius:8px;text-align:center;color:var(--white)}
.quote p{margin-top:35px;font-size:15px}
.quote h3{font-size:22px;font-weight:500;margin-top:4px}
.field{position:absolute;left:35px;width:266px;height:35px;border-radius:18px;background:var(--mint-card);font-size:11px;color:#9aaca6;text-align:left;padding:10px 20px}
.center{text-align:center;left:0;width:1200px}
.svc{position:absolute;top:961px;width:200px;text-align:center}
.svc h4{margin-top:128px;font-size:18px;font-weight:500;color:var(--green-dark)}
.svc p{margin-top:12px;font-size:13px;line-height:20px}
.svc-icon{position:absolute;left:42px;top:0}
.feature{position:absolute;left:0;top:1272px;width:1200px;height:557px;background:var(--grey-bg)}
.checks{position:absolute;left:705px;top:1576px;list-style:none;font-size:13px;font-weight:500;color:var(--green-dark)}
.checks li{display:flex;align-items:center;gap:8px;height:30.5px}
.reviews{position:absolute;left:0;top:2421px;width:1200px;height:620px;background:var(--green-dark)}
.card{position:absolute;top:2658px;width:272px;height:310px;background:var(--mint-card);border-radius:6px;padding:0 34px}
.card .stars{margin-top:100px;color:var(--orange);font-size:16px;letter-spacing:6px}
.card h5{margin-top:8px;font-size:17px;font-weight:600;color:var(--green-dark)}
.card p{margin-top:10px;font-size:13px;line-height:20px}
.card b{display:block;margin-top:12px;font-size:13px;color:var(--green-dark);font-weight:600}
.avatar{position:absolute;top:-50px;left:34px;width:116px;height:116px;border-radius:50%}
.press{position:absolute;top:3174px;width:170px;text-align:center;font-size:28px;color:#55606a;font-weight:600}
.footer{position:absolute;left:0;top:3747px;width:1200px;height:325px;background:var(--mint)}
.flinks{position:absolute;left:529px;top:3830px;list-style:none;font-size:12px;color:var(--green-dark)}
.flinks li{height:33.8px}
.fcontact{position:absolute;left:682px;display:flex;gap:10px;font-size:13px;color:var(--green-dark);line-height:17px}
.copy{position:absolute;left:0;top:4072px;width:1200px;height:55px;background:var(--green-dark);color:#9cc0b4;font-size:12px;display:flex;align-items:center;justify-content:center}
</style>
</head>
<body>

<section class="hero">
  <div class="hero-band"></div>
</section>

<header>
  <div class="brand abs" style="left:58px;top:26px"><span class="brand-dot"></span>Tailbrook</div>
  <nav class="nav"><span>Locations</span><span>Careers</span><span>About</span><span>Blog</span><span>FAQ</span></nav>
  <div class="phone" style="left:823px;top:32px">
    <svg width="22" height="22" viewBox="0 0 24 24" fill="none" stroke="#0d5a4a" stroke-width="1.6"><path d="M5 3h4l2 5-3 2a11 11 0 0 0 6 6l2-3 5 2v4a2 2 0 0 1-2 2A17 17 0 0 1 3 5a2 2 0 0 1 2-2z"/></svg>
    <div><strong>(+014) 586 -902</strong><small>Call, Text, or</small></div>
  </div>
  <a class="btn" style="left:1011px;top:29px;width:129px;height:29px">Book Online</a>
</header>

<div class="abs hero-kicker">Lorem ipsum dolor</div>
<h1 class="abs hero-title">Dog<br>Grooming</h1>
<p class="abs hero-text">Sed ut perspiciatis unde omnis iste natus error sit volup tatem accusantium dolo remque laudantium, totam rem aperiam, eaque ipsa quae ab illo inventore verita tis et quasi architecto bea.</p>
<svg class="abs" style="left:365px;top:475px" width="125" height="60" viewBox="0 0 125 60" fill="none" stroke="#0d5a4a" stroke-width="1.4"><path d="M3 3C20 35 60 52 112 54" stroke-dasharray="4 4"/><path d="M112 48l8 6-8 5z" fill="#0d5a4a"/></svg>

<form class="quote">
  <p>Get Free Quotes from</p>
  <h3>Grooming Specialists!</h3>
  <div class="field" style="top:112px">Name*</div>
  <div class="field" style="top:163px">Email*</div>
  <div class="field" style="top:213px">Phone*</div>
  <div class="field" style="top:263px">State*<svg style="position:absolute;right:20px;top:14px" width="10" height="7"><path d="M0 0h10L5 7z" fill="#0d5a4a"/></svg></div>
  <a class="btn" style="left:86px;top:314px;width:164px;height:34px">Get A Quote Now</a>
</form>

<div class="photo" role="img" aria-label="Bulldog in a yellow hoodie looking over its shoulder" style="left:812px;top:184px;width:388px;height:482px;border-radius:160px 0 0 0;background:linear-gradient(160deg,#d8c3ad,#e3b94a 55%,#c8a88a)"></div>

<h2 class="abs h2 center" style="top:748px">Sed ut perspiciatis unde<br>omnis iste</h2>
<p class="abs center" style="top:852px;font-size:13px;line-height:20px">Sed ut perspiciatis unde omnis iste natus error sit volup tatem accusantium dolo remque laudantium,<br>totam rem aperiam, eaque ipsa quae ab illo inventore verita tis et quasi architecto bea.</p>

<div class="svc" style="left:156px">
  <div class="svc-icon" role="img" aria-label="Dog head line icon" style="width:116px;height:116px;border-radius:50%;background:var(--mint)"></div>
  <h4>Quis autem vel</h4><p>Lorem ipsum dolor sit amet, consec tetur adipiscing elit, sed do eiusmod tempor.</p>
</div>
<div class="svc" style="left:384px">
  <div class="svc-icon" role="img" aria-label="Dog bowl line icon" style="width:116px;height:116px;border-radius:50%;background:var(--mint)"></div>
  <h4>Nemo enim ipsam</h4><p>Lorem ipsum dolor sit amet, consec tetur adipiscing elit, sed do eiusmod tempor.</p>
</div>
<div class="svc" style="left:613px">
  <svg class="svc-icon" role="img" aria-label="Pet carrier line icon" width="116" height="116" viewBox="0 0 116 116"><circle cx="58" cy="58" r="58" fill="#0d5a4a"/><path d="M14 30C22 8 50 0 60 12c8 10-6 24-20 26-14 2-30 4-26-8z" fill="#fa8a6a"/></svg>
  <h4>Quis autem vel</h4><p>Lorem ipsum dolor sit amet, consec tetur adipiscing elit, sed do eiusmod tempor.</p>
</div>
<div class="svc" style="left:840px">
  <div class="svc-icon" role="img" aria-label="Dog walking line icon" style="width:116px;height:116px;border-radius:50%;background:var(--mint)"></div>
  <h4>Nemo enim ipsam</h4><p>Lorem ipsum dolor sit amet, consec tetur adipiscing elit, sed do eiusmod tempor.</p>
</div>

<section class="feature">
  <div class="photo" role="img" aria-label="Long-haired small dog with bows being combed" style="left:0;top:0;width:770px;height:557px;background:linear-gradient(120deg,#e9ecee 10%,#b9a591 40%,#d8ccc0 65%,#eef1f2 90%)"></div>
</section>
<h2 class="abs h2" style="left:705px;top:1343px">Lorem ipsum dolor<br>sit amet consecte<br>tur adipiscing</h2>
<p class="abs" style="left:705px;top:1491px;width:330px;font-size:13px;line-height:20px">Sed ut perspiciatis unde omnis iste natus error sit volup tatem accusantium dolo remque laudantium, totam rem aperiam, eaque ipsa quae.</p>
<ul class="checks">
  <li><svg width="20" height="20"><circle cx="10" cy="10" r="10" fill="#0d5a4a"/><path d="M5.5 10l3 3 6-6" stroke="#fff" stroke-width="2" fill="none"/></svg>Ut enim ad minim veniamquis nostrud</li>
  <li><svg width="20" height="20"><circle cx="10" cy="10" r="10" fill="#0d5a4a"/><path d="M5.5 10l3 3 6-6" stroke="#fff" stroke-width="2" fill="none"/></svg>Exercitation ullamco laboris nisi ut</li>
  <li><svg width="20" height="20"><circle cx="10" cy="10" r="10" fill="#0d5a4a"/><path d="M5.5 10l3 3 6-6" stroke="#fff" stroke-width="2" fill="none"/></svg>Aliquip ex ea commodo consequat</li>
  <li><svg width="20" height="20"><circle cx="10" cy="10" r="10" fill="#0d5a4a"/><path d="M5.5 10l3 3 6-6" stroke="#fff" stroke-width="2" fill="none"/></svg>Duis aute irure dolor in</li>
</ul>
<a class="btn" style="left:705px;top:1717px;width:163px;height:36px">Book Online</a>

<div class="photo" role="img" aria-label="Hand holding a purple hair dryer" style="left:0;top:2083px;width:305px;height:320px;background:linear-gradient(110deg,#f3e6de 20%,#9b3fd0 55%,#ffffff 90%)"></div>
<div class="photo" role="img" aria-label="Golden retriever lying down and smiling" style="left:689px;top:1915px;width:511px;height:506px;background:radial-gradient(circle at 60% 40%,#d9973f,#e7b573 45%,#f6f1ea 80%)"></div>
<h2 class="abs h2" style="left:322px;top:1958px">Neque porro quisquam<br>est qui dolorem</h2>
<p class="abs" style="left:322px;top:2068px;width:385px;font-size:13px;line-height:20px">Sed ut perspiciatis unde omnis iste natus error sit volup tatem accusantium doloremque laudantium, totam rem aperiam, eaque ipsa quae ab illo inventore veritatis et quasi architecto beatae vitae dicta sunt explicabo.</p>
<p class="abs" style="left:322px;top:2169px;width:385px;font-size:13px;line-height:20px">Lorem ipsum dolor sit amet, consectetur adipiscing elit, sed do eiusmod tempor incididunt ut labore et dolore magna aliqua. Ut enim ad minim veniam.</p>
<div class="phone" style="left:322px;top:2268px">
  <svg width="22" height="22" viewBox="0 0 24 24" fill="none" stroke="#0d5a4a" stroke-width="1.6"><path d="M5 3h4l2 5-3 2a11 11 0 0 0 6 6l2-3 5 2v4a2 2 0 0 1-2 2A17 17 0 0 1 3 5a2 2 0 0 1 2-2z"/></svg>
  <div><strong>(+014) 586 -902</strong><small>Call, Text, or</small></div>
</div>
<a class="btn" style="left:514px;top:2270px;width:165px;height:34px">Book Online</a>

<section class="reviews">
  <h2 class="abs" style="left:159px;top:80px;font-size:35px;font-weight:600;color:var(--white)">What Our Customers Say</h2>
  <svg class="abs" style="left:953px;top:86px" width="90" height="22" viewBox="0 0 90 22" fill="none" stroke-width="2"><path d="M36 11H2m9-8-9 8 9 8" stroke="#ffffff"/><path d="M54 11h34m-9-8 9 8-9 8" stroke="#fa8a6a"/></svg>
</section>
<article class="card" style="left:157px">
  <div class="avatar" role="img" aria-label="Dog wearing sunglasses" style="background:radial-gradient(circle,#e0a15a,#8b4a25)"></div>
  <div class="stars">★★★★★</div><h5>Amazing Service</h5>
  <p>sit volup tatem accusantium do loremque laudantium, totam rem aperiam, eaque ipsa quae ab illo inventore veritatis et quasi architecto beatae vitae</p><b>John Doe</b>
</article>
<article class="card" style="left:463px">
  <div class="avatar" role="img" aria-label="Groomer holding a small white dog" style="background:radial-gradient(circle,#f0ece6,#b07a55)"></div>
  <div class="stars">★★★★★</div><h5>Great Pricing</h5>
  <p>sit volup tatem accusantium do loremque laudantium, totam rem aperiam, eaque ipsa quae ab illo inventore veritatis et quasi architecto beatae vitae</p><b>Marcus Vale</b>
</article>
<article class="card" style="left:767px">
  <div class="avatar" role="img" aria-label="Brown dog after a grooming session" style="background:radial-gradient(circle,#b06a3c,#d9d4cc)"></div>
  <div class="stars">★★★★★</div><h5>Recomended</h5>
  <p>sit volup tatem accusantium do loremque laudantium, totam rem aperiam, eaque ipsa quae ab illo inventore veritatis et quasi architecto beatae vitae</p><b>Nora Quill</b>
</article>

<p class="abs center" style="top:3117px;font-size:18px;color:var(--green-dark)">As Seen In</p>
<div class="press" style="left:128px;font-weight:400">Velour Home</div>
<div class="press" style="left:304px">Gentry</div>
<div class="press" style="left:500px">Metro Daily</div>
<div class="press" style="left:702px">Ledgerline</div>
<div class="press" style="left:905px;font-weight:400">Tillpoint</div>

<div class="photo" role="img" aria-label="Golden retriever being rinsed with a shower head" style="left:0;top:3295px;width:1200px;height:452px;background:linear-gradient(100deg,#e9e4de 15%,#c89566 45%,#8c5a35 60%,#efebe6 90%)"></div>
<svg class="abs" style="left:562px;top:3482px" width="76" height="76" viewBox="0 0 76 76"><circle cx="38" cy="38" r="38" fill="#fa8a6a"/><path d="M31 27l17 11-17 11z" fill="#fff"/></svg>

<footer class="footer">
  <div class="brand abs" style="left:159px;top:84px"><span class="brand-dot"></span>Tailbrook</div>
  <p class="abs" style="left:159px;top:155px;width:275px;font-size:13px;line-height:20px">Lorem ipsum dolor sit amet, consectetur ad ipiscing elit, sed do eiusmod tempor incidi dunt ut labore et dolore magna aliqua. Ut enim ad minim veniam.</p>
</footer>
<ul class="flinks"><li>Locations</li><li>Careers</li><li>About</li><li>Blog</li><li>FAQ</li></ul>
<div class="phone" style="left:682px;top:3834px">
  <svg width="22" height="22" viewBox="0 0 24 24" fill="none" stroke="#0d5a4a" stroke-width="1.6"><path d="M5 3h4l2 5-3 2a11 11 0 0 0 6 6l2-3 5 2v4a2 2 0 0 1-2 2A17 17 0 0 1 3 5a2 2 0 0 1 2-2z"/></svg>
  <div><strong>(+014) 586 -902</strong><small>Call, Text, or</small></div>
</div>
<a class="btn" style="left:876px;top:3835px;width:164px;height:34px">Book Online</a>
<div class="fcontact" style="top:3898px">
  <svg width="20" height="18" viewBox="0 0 20 18" fill="none" stroke="#0d5a4a" stroke-width="1.6"><rect x="1" y="2" width="18" height="14" rx="2"/><path d="M1 4l9 6 9-6"/></svg>
  <span>info@tailbrookgrooming.com</span>
</div>
<div class="fcontact" style="top:3934px">
  <svg width="20" height="22" viewBox="0 0 20 22" fill="none" stroke="#0d5a4a" stroke-width="1.6"><path d="M10 21s7-7 7-12a7 7 0 0 0-14 0c0 5 7 12 7 12z"/><circle cx="10" cy="9" r="2.5"/></svg>
  <span>123, Lorem ipsum dolor sit amet,<br>consectetur Adipiscing</span>
</div>
<div class="copy">© Copyright 2021 Tailbrook. All rights reserved.</div>

</body>
</html>
```